Redesign a TV Station website

Hello,
it looks like my explaination was not clear enough so i would like to clarify.
We are no longer designing a news website but rather a website for our TV station.
Please take a look at the current website we have .
http://www.vko.ci
We want a website similar to these two websites as example.

Please use the following websites as example
https://www.lumatel.com/
https://www.drw.com/

Here are my main menu on the horizontal bar
Accueil | Films | Series | Enfants | TV en Direct
P/S: You should disregard previous designs for the news website. We are designing purely a website for the TV stations. Please take a look at current site we have and design it similar to these two examples i mentioned
https://www.lumatel.com/
https://www.drw.com/
Updates

I needed more info for the project update.

Hello, We have updated design requirement for our project and hope it is much easier for you. You need to design the page based on the content on the link below: http://587opratv.com/template_obs.pdf You should use the same design as this to design the page http://587opratv.com/marc.jpeg The page will have same header style, color and design as the last link. However the content and layout of the page is the same as the first link. Please disregard the section that says "PAGE TYPE POUR MOBILE VERSION" Also disregard the title "MINI SITE LES ARPENTEURS "

Target Market(s)

TV Station

Number of Pages Required

1 page

Font styles to use
Sans Serif

Colors

Designer to choose colors to be used in the design.

Requirements
Must have
• N/A
Nice to have
• N/A
Should not have
• N/A

```html
<!DOCTYPE html>
<html lang="fr">
<head>
<meta charset="utf-8">
<title>Kalima TV</title>
<link href="https://fonts.googleapis.com/css2?family=Poppins:wght@400;500;600;700&display=swap" rel="stylesheet">
<style>
:root{
  --orange:#f08232;
  --orange-dark:#e56f1e;
  --ink:#1d1d1f;
  --text:#555;
  --muted:#777;
  --line:#e6e6e6;
  --blue:#1e8fe1;
  --white:#fff;
}
*{box-sizing:border-box;margin:0;padding:0}
html,body{width:1200px;height:3192px;overflow:hidden;background:var(--white);font-family:'Poppins',sans-serif;color:var(--ink)}
.page{position:relative;width:1200px;height:3192px}
.abs{position:absolute}
/* header */
.brand{left:66px;top:30px;display:flex;align-items:center;gap:10px;font-size:34px;font-weight:600;color:var(--ink);white-space:nowrap}
.brand i{display:block;width:22px;height:22px;background:var(--orange)}
.ad-banner{left:311px;top:20px;width:460px;height:56px;background:linear-gradient(90deg,#3fa3b5,#2e8fa6);display:flex;align-items:center;justify-content:center;color:#fff;font-weight:600;font-size:16px;line-height:1.15;text-align:center}
.social{top:33px;display:flex;gap:8px;left:796px}
.social i{display:block;width:30px;height:30px;border-radius:4px}
.header-btn{top:32px;height:31px;padding:0 10px;display:flex;align-items:center;color:#fff;font-size:12px;font-weight:600;border-radius:3px}
.btn-videos{left:967px;background:var(--blue)}
.btn-podcasts{left:1044px;background:var(--orange)}
.main-nav{left:66px;top:97px;width:1066px;height:49px;background:var(--orange);display:flex;align-items:center}
.nav-burger{width:50px;height:49px;background:var(--orange-dark);display:flex;align-items:center;justify-content:center}
.nav-links{display:flex;gap:30px;margin-left:86px;font-size:12px;font-weight:600;color:#fff}
.nav-search{margin-left:auto;width:52px;height:49px;background:var(--orange-dark);display:flex;align-items:center;justify-content:center}
/* hero */
.hero{left:66px;top:146px;width:1066px;height:546px;background:radial-gradient(ellipse at 35% 40%,#6a6a68,#3a3a38 60%,#2a2a28)}
.tag{display:inline-block;background:var(--orange);color:#fff;font-size:10px;font-weight:600;padding:2px 7px;text-transform:uppercase}
.hero-caption{position:absolute;left:68px;top:368px;color:#fff}
.hero-caption h1{font-size:25px;font-weight:600;line-height:1.25;margin-top:8px;width:560px}
.date{display:flex;align-items:center;gap:6px;font-size:12px;font-weight:600;margin-top:12px}
.date i{width:14px;height:14px;border-radius:50%;background:var(--blue)}
.latest{left:755px;top:198px;width:329px;height:442px;background:#fff;padding:30px 34px}
.latest h2{font-size:19px;font-weight:600;letter-spacing:.3px;margin-bottom:18px}
.latest-list{border-left:2px solid var(--orange);padding-left:20px}
.latest-item{display:flex;gap:14px;margin-bottom:22px}
.latest-time{width:46px;flex:none;text-align:center;font-size:12px;font-weight:700}
.latest-time b{display:block;background:var(--orange);color:#fff;padding:1px 0;margin-bottom:6px}
.latest-item p{font-size:13px;line-height:1.35;color:#333;width:185px}
.more{position:absolute;right:26px;bottom:36px;font-size:11px;color:var(--orange);font-weight:600;text-decoration:underline}
/* section heads */
.sec-head{height:43px;border-bottom:2px solid #f4c4a0}
.sec-head span{display:inline-block;height:43px;line-height:43px;padding:0 15px;background:var(--orange);color:#fff;font-size:17px;font-weight:600}
/* cards */
.card{width:746px;height:273px;background:#fff;border:1px solid #eee;box-shadow:0 1px 4px rgba(0,0,0,.06)}
.card-body{position:absolute;left:31px;top:28px;width:452px}
.card h3{font-size:18px;font-weight:600;line-height:1.4;margin-top:10px}
.card p{font-size:13px;line-height:1.5;color:var(--text);margin-top:8px;text-align:justify}
.card-meta{position:absolute;left:31px;bottom:18px;width:445px;border-top:1px solid var(--line);padding-top:18px;font-size:13px;color:var(--muted)}
.card-meta em{font-style:normal;margin-left:24px}
.card-img{position:absolute;left:508px;top:18px;width:221px;height:237px}
.tile{width:266px;height:183px}
.tile-caption{position:absolute;left:20px;bottom:16px;color:#fff}
.tile-caption b{font-size:15px;font-weight:600}
.tile-caption .date{margin-top:2px;font-size:11px}
.popular{left:866px;top:1546px;width:266px;height:394px;border:1px solid #eee;padding:22px 12px 0 16px}
.pop-item{display:flex;gap:12px;padding-bottom:24px;margin-bottom:22px;border-bottom:1px solid var(--line)}
.pop-item:last-child{border:none}
.pop-item b{font-family:Georgia,serif;font-size:40px;font-weight:400;line-height:1}
.pop-item p{font-size:13px;color:#444;line-height:1.35}
.photo-row{left:66px;top:2072px;display:flex;gap:14px}
.photo-row div{width:256px;height:219px}
.page-links{left:0;top:2330px;width:1200px;text-align:center;font-size:17px;font-weight:500;letter-spacing:.3px}
.partners{left:66px;top:2394px;width:1066px}
.partner-logos{left:110px;top:2482px;display:flex;align-items:center;width:980px;justify-content:space-between}
.plan{left:66px;top:2630px;width:1066px;height:60px;border-top:2px solid #222;border-bottom:2px solid #222}
.plan h2{font-size:29px;font-weight:600;line-height:56px}
.col{top:2752px}
.col h4{font-size:13px;font-weight:600;margin-bottom:18px}
.col ul{list-style:none;font-size:13px;color:#444;line-height:19.6px}
.sep{top:2752px;width:1px;height:325px;background:var(--line)}
.store{width:161px;height:54px;background:#111;border-radius:8px;color:#fff;display:flex;align-items:center;gap:10px;padding-left:14px;white-space:nowrap}
.store i{width:28px;height:28px;flex:none;border-radius:50%;background:#fff}
.store small{display:block;font-size:8px;line-height:1.3}
.store b{font-size:16px;font-weight:600;line-height:1.1}
.foot{left:66px;top:3138px;width:1066px;border-top:1px solid var(--line);padding-top:17px;text-align:center;font-size:12px;color:#222}
.to-top{left:1144px;top:3116px;width:42px;height:42px;border-radius:50%;background:var(--orange);display:flex;align-items:center;justify-content:center}
</style>
</head>
<body>
<div class="page">
  <header>
    <div class="abs brand"><i></i>Kalima TV</div>
    <div class="abs ad-banner" role="img" aria-label="Bannière climat">AGIR POUR LE CLIMAT...<br>OUI, MAIS COMMENT ?</div>
    <div class="abs social" aria-label="Réseaux sociaux">
      <i style="background:#3b5998"></i><i style="background:#1da1f2"></i><i style="background:#c13584"></i><i style="background:#25b14a"></i>
    </div>
    <a class="abs header-btn btn-videos">VIDEOS</a>
    <a class="abs header-btn btn-podcasts">PODCASTS</a>
    <nav class="abs main-nav">
      <div class="nav-burger"><svg width="18" height="14"><path d="M0 1h18M0 7h18M0 13h18" stroke="#fff" stroke-width="2"/></svg></div>
      <div class="nav-links"><span>POLITIQUE</span><span>ECONIMIE</span><span>SOCIETE</span><span>CULTURE</span><span>REGION</span><span>SPORTS</span><span>TECHNOLOGIE</span><span>AFRIQUE</span><span>INTERNATIONAL</span></div>
      <div class="nav-search"><svg width="16" height="16"><circle cx="6.5" cy="6.5" r="5" fill="none" stroke="#fff" stroke-width="1.6"/><path d="M10 10l5 5" stroke="#fff" stroke-width="1.6"/></svg></div>
    </nav>
  </header>

  <section class="abs hero" role="img" aria-label="Photo à la une : deux hommes en costume posant ensemble">
    <div class="hero-caption">
      <span class="tag">World</span>
      <h1>Rome: un escalier mecanique s' ecroule, une vingtaine de blesses</h1>
      <div class="date"><i></i>SUNDAY JULY 14 2019</div>
    </div>
  </section>
  <aside class="abs latest">
    <h2>DRNIERES NOUVELLES</h2>
    <div class="latest-list">
      <div class="latest-item"><div class="latest-time"><b>01:33</b>APN</div><p>Cursus a sit amet mauris morbi ipsum velit nam nec tellus...</p></div>
      <div class="latest-item"><div class="latest-time"><b>01:33</b>APN</div><p>Cursus a sit amet mauris morbi ipsum velit nam nec tellus...</p></div>
      <div class="latest-item"><div class="latest-time"><b>01:33</b>APN</div><p>Cursus a sit amet mauris morbi ipsum velit nam nec tellus...</p></div>
      <div class="latest-item"><div class="latest-time"><b>01:33</b>APN</div><p>Cursus a sit amet mauris morbi ipsum velit nam nec tellus...</p></div>
    </div>
    <span class="more">VOIR PLUS...</span>
  </aside>

  <div class="abs sec-head" style="left:66px;top:745px;width:746px"><span>LES AUTRES ARTICLES</span></div>
  <div class="abs sec-head" style="left:866px;top:745px;width:266px"><span>L'EQUIPE</span></div>

  <article class="abs card" style="left:66px;top:824px">
    <div class="card-body"><span class="tag">Decryptages</span><h3>Correlation et causallte : peut-on decrocher un prix Nobel en mangeant du chocolat ?</h3><p>Ur article sc,enti,que pub, er 20. assure que la consormation de chocolatioue un role darts robtention de pnx Nobel. En realrte, cet article etait une blague. Lauteur de [etude voulait avant tout alerter sur les correlations trompeuses.</p></div>
    <div class="card-meta">PubGi aujourclhu. 11.15,14 ijour 1181151</div>
    <div class="card-img" role="img" aria-label="Photo de dirigeants européens en réunion" style="background:linear-gradient(135deg,#8a5a3c,#c49a78 50%,#3e4a6a)"></div>
  </article>
  <article class="abs card" style="left:66px;top:1107px">
    <div class="card-body"><span class="tag">Decryptages</span><h3>Pourquol certalnes Insultes restent homophobes malgre leur banallsat</h3><p>Encule pede s; ces ,nsuites qui fuser, no:arnment dans les stades, ne sort pas toujours consciernrnent homophobes, elles n'en sort pas moins discriminatoires. Explications.</p></div>
    <div class="card-meta">Pub,eaujourd ha, 11.13, m,s aiour a 161,08<em>Assia Mando</em></div>
    <div class="card-img" role="img" aria-label="Portrait d'un homme âgé à lunettes" style="background:linear-gradient(135deg,#6c6f76,#c8a99a 55%,#2a3142)"></div>
  </article>

  <div class="abs tile" style="left:866px;top:814px;background:linear-gradient(160deg,#8a7a66,#4a4a50 60%,#2c3040)" role="img" aria-label="Photo d'un orateur à un pupitre"><div class="tile-caption"><b>Jos: Le Journal Des Sports</b><div class="date"><i></i>Sunday july 14 2019</div></div></div>
  <div class="abs tile" style="left:866px;top:1007px;background:linear-gradient(160deg,#555,#3a3c44 60%,#222630)" role="img" aria-label="Photo de deux hommes en costume"><div class="tile-caption"><b>Jos: Le Journal Des Sports</b><div class="date"><i></i>Sunday july 14 2019</div></div></div>
  <div class="abs tile" style="left:866px;top:1197px;background:linear-gradient(160deg,#3c3c3c,#7a6050 55%,#1e2030)" role="img" aria-label="Portrait d'un homme en costume"><div class="tile-caption"><b>Jos: Le Journal Des Sports</b><div class="date"><i></i>Sunday july 14 2019</div></div></div>

  <article class="abs card" style="left:66px;top:1476px">
    <div class="card-body"><span class="tag">Decryptages</span><h3>Correlation et causallte : peut-on decrocher un prix Nobel en mangeant du chocolat ?</h3><p>Ur article sc,enti,que pub, er 20. assure que la consormation de chocolatioue un role darts robtention de pnx Nobel. En realrte, cet article etait une blague. Lauteur de [etude voulait avant tout alerter sur les correlations trompeuses.</p></div>
    <div class="card-meta">PubGi aujourclhu. 11.15,14 ijour 1181151</div>
    <div class="card-img" role="img" aria-label="Photo de deux hommes en costume souriant" style="background:linear-gradient(135deg,#c9b8a8,#8a96b0 50%,#2a3048)"></div>
  </article>
  <article class="abs card" style="left:66px;top:1759px">
    <div class="card-body"><span class="tag">Decryptages</span><h3>Pourquol certalnes Insultes restent homophobes malgre leur banallsat</h3><p>Encule pede s; ces ,nsuites qui fuser, no:arnment dans les stades, ne sort pas toujours consciernrnent homophobes, elles n'en sort pas moins discriminatoires. Explications.</p></div>
    <div class="card-meta">Pub,eaujourd ha, 11.13, m,s aiour a 161,08<em>Assia Mando</em></div>
    <div class="card-img" role="img" aria-label="Photo d'un homme saluant la foule" style="background:linear-gradient(135deg,#d8cfc4,#6a5448 50%,#2a2a30)"></div>
  </article>

  <div class="abs sec-head" style="left:866px;top:1476px;width:266px"><span>LES PLUS LUS</span></div>
  <aside class="abs popular">
    <div class="pop-item"><b>1</b><p>Coupe du monde de basket 2oig la presse americaine fataliste apres la defaite de 9 Team Nordia</p></div>
    <div class="pop-item"><b>2</b><p>Fraude fiscale : Searchix va verser p.s thin milliard creuros pour clore les poursuites en France</p></div>
    <div class="pop-item"><b>3</b><p>Pesticides : a 'l, ',est plus temps de faire semblant de prendre des deml-mesures</p></div>
  </aside>

  <div class="abs photo-row">
    <div role="img" aria-label="Photo d'un jeune homme au chapeau de paille" style="background:linear-gradient(160deg,#8a6a4c,#c8b49a 50%,#5a6a80)"></div>
    <div role="img" aria-label="Portrait d'un homme à lunettes dans une salle sombre" style="background:linear-gradient(160deg,#2c2622,#5a4a3c 55%,#1a1a1e)"></div>
    <div role="img" aria-label="Portrait d'un homme en costume et cravate rouge" style="background:linear-gradient(160deg,#b07a4a,#6a4030 55%,#2a2c38)"></div>
    <div role="img" aria-label="Portrait d'un homme s'exprimant au micro" style="background:linear-gradient(160deg,#1e1e22,#4a3a30 55%,#151518)"></div>
  </div>

  <nav class="abs page-links">LES VERIFICATEURS &nbsp;|&nbsp; LA COMMUNAUTE &nbsp;|&nbsp; NOUS JOINDRE &nbsp;|&nbsp; LA CHARTE</nav>

  <div class="abs sec-head partners"><span>PARTENAIRES</span></div>
  <div class="abs partner-logos" aria-label="Partenaires">
    <svg width="90" height="86"><rect width="90" height="86" fill="#2a8fe0"/></svg>
    <svg width="170" height="40"><rect width="170" height="40" rx="4" fill="#222"/></svg>
    <svg width="88" height="86"><rect width="88" height="86" fill="#e3262e"/></svg>
    <svg width="142" height="60"><circle cx="30" cy="30" r="28" fill="#555"/><rect x="66" y="16" width="76" height="28" rx="4" fill="#777"/></svg>
    <svg width="88" height="86"><rect width="88" height="86" fill="#4fae3a"/></svg>
    <svg width="138" height="64"><circle cx="100" cy="32" r="30" fill="#9cc4ec"/><rect x="0" y="18" width="80" height="28" rx="4" fill="#1d5fb8"/></svg>
  </div>

  <div class="abs plan"><h2>PLAN DU SITE</h2></div>
  <div class="abs col" style="left:66px"><h4>EN CONTINU</h4><ul><li>Flash Info</li><li>Demieres Nouvelles</li><li>Politique</li><li>Economie</li><li>Societe</li><li>Culture</li><li>Region</li><li>Technologie</li><li>Afrique</li><li>International</li><li>Reveue de Presse</li><li>Interviews</li><li>Reportages</li><li>Dossier</li><li>Enquete</li></ul></div>
  <div class="abs sep" style="left:279px"></div>
  <div class="abs col" style="left:390px"><h4>REPLY</h4><ul><li>Journaux</li><li>Magazine</li><li>Reportages</li></ul>
    <h4 style="margin-top:38px">SUIVRE L'INFO</h4><ul><li>Visagram</li><li>Pépieur</li><li>Instantané</li><li>Quoi9</li><li>Alert Sms</li><li>Newsletter</li><li>Flux Rss</li></ul></div>
  <div class="abs sep" style="left:579px"></div>
  <div class="abs col" style="left:674px"><h4>PARTICIPER</h4><ul><li>Think Tank Le</li><li>Le Sondage</li><li>Contactez Kalima Info</li></ul>
    <h4 style="margin-top:42px">LES VERIFICATEURS</h4><ul><li>Les Verificateurs</li><li>La Communates</li><li>Les Articles</li><li>Le Equipe</li></ul></div>
  <div class="abs sep" style="left:888px"></div>
  <div class="abs col" style="left:971px"><h4>TELECHARGEZ</h4>
    <div class="store"><i></i><div><small>GET IT ON</small><b>Kiosque Play</b></div></div>
    <div class="store" style="margin-top:8px"><i></i><div><small>GET IT ON</small><b>Boutique</b></div></div>
  </div>

  <footer class="abs foot">Mentionslegales &nbsp;I&nbsp; Conditions generales d,utilisation &nbsp;I&nbsp; Plitique de protection &nbsp;I&nbsp; Cookies &nbsp;I&nbsp; CGU &nbsp;I&nbsp; Contacts</footer>
  <a class="abs to-top" aria-label="Haut de page"><svg width="14" height="16"><path d="M7 15V2M2 7l5-5 5 5" fill="none" stroke="#fff" stroke-width="1.6"/></svg></a>
</div>
</body>
</html>
```